Autism Center Needs a Brochure Design

We are looking for a new and improved brochure design for our Autism Center serving Northern Indiana. We provide ABA therapy for children who are on the autism spectrum. We would like to see designs that reflect some of our other marketing material and use our companies colors (blue, yellow and green). For more specific colors, look at our company logo I have uploaded below. I have also uploaded a outline of all of the information we want in the brochure and what content we want on each page.
- Calibri, Times

```html
<!DOCTYPE html>
<html lang="en">
<head>
<meta charset="utf-8">
<title>Autism Center Brochure – Inside Spread</title>
<link href="https://fonts.googleapis.com/css2?family=Oswald:wght@400&family=Open+Sans:wght@400;600&display=swap" rel="stylesheet">
<style>
  :root{
    --blue:#1a72bf;
    --blue-dark:#0f4f8c;
    --blue-text:#2a7cc4;
    --green:#2ead5d;
    --yellow:#f6c21c;
    --ink:#333333;
    --white:#ffffff;
  }
  *{box-sizing:border-box;margin:0;padding:0}
  html,body{width:1200px;height:932px;overflow:hidden;background:var(--white)}
  .spread{position:relative;width:1200px;height:932px;font-family:"Open Sans",Arial,sans-serif;color:var(--ink)}

  /* left column */
  .left-photo{position:absolute;left:0;top:0;width:404px;height:374px;
    background:linear-gradient(135deg,#c9b8a0 0%,#e6d7c2 35%,#b9a58d 60%,#c6383a 85%,#d44a45 100%)}
  .aba-panel{position:absolute;left:0;top:374px;width:404px;height:558px;background:var(--green)}
  .aba-ribbon{position:absolute;left:0;top:17px;width:305px;height:48px}
  .aba-ribbon span{position:absolute;left:70px;top:6px;font-family:"Oswald",sans-serif;font-size:24px;color:var(--white)}
  .mark-dot{position:absolute;left:228px;top:10px;width:30px;height:30px;border-radius:50%;background:var(--white)}
  .aba-list{position:absolute;left:36px;top:74px;list-style:none;font-family:"Oswald",sans-serif;font-size:21px;line-height:32.5px;color:var(--white)}
  .aba-list li{padding-left:16px;text-indent:-16px}
  .aba-list li::before{content:"• "}
  .aba-list li.tight{line-height:24px;margin-top:4px}
  .session-photo{position:absolute;left:33px;top:269px;width:350px;height:263px;border:6px solid var(--yellow);border-radius:20px;
    background:linear-gradient(120deg,#d9d4c4 0%,#eeeae0 45%,#9bc1d8 70%,#3e3f49 100%)}

  /* ribbons */
  .ribbon{position:absolute;height:52px}
  .ribbon svg{position:absolute;inset:0}
  .ribbon span{position:relative;display:block;text-align:center;font-family:"Oswald",sans-serif;font-size:24px;line-height:44px;color:var(--white)}
  .help-ribbon{left:420px;top:40px;width:366px}
  .difference-ribbon{left:815px;top:40px;width:366px}

  .copy{position:absolute;left:429px;width:352px;font-size:13.6px;line-height:18px;text-align:justify}
  .copy em{font-style:normal;font-weight:600;color:var(--blue-text)}
  .copy p+p{margin-top:6px}
  .help-copy{top:118px}
  .approach-copy{top:708px}

  .feature-list{position:absolute;left:818px;list-style:none;font-family:"Oswald",sans-serif;font-size:21px;line-height:36px;color:var(--blue)}
  .feature-list li::before{content:"• "}
  .difference-list{top:124px}
  .service-list{top:720px}

  .team-photo{position:absolute;left:404px;top:215px;width:796px;height:495px;
    background:linear-gradient(180deg,#e8eef2 0%,#8a8a5e 22%,#5d6a3a 42%,#3c4a5e 55%,#5f8a3a 72%,#6f9c45 100%);
    -webkit-mask-image:linear-gradient(180deg,transparent 0%,#000 14%,#000 82%,transparent 100%);
            mask-image:linear-gradient(180deg,transparent 0%,#000 14%,#000 82%,transparent 100%)}
</style>
</head>
<body>
<main class="spread">

  <div class="left-photo" role="img" aria-label="Photo of a therapist playing a hand game with two young boys in a bright classroom"></div>

  <section class="aba-panel">
    <div class="aba-ribbon">
      <svg width="305" height="48" viewBox="0 0 305 48">
        <polygon points="0,0 305,0 285,24 305,48 0,48" fill="var(--blue)"/>
      </svg>
      <span>ABA Therapy</span>
      <i class="mark-dot"></i>
    </div>
    <ul class="aba-list">
      <li>Develops new skills</li>
      <li>Refines previously learned skills</li>
      <li>Decreases socially deviant behaviors</li>
      <li>It is endorsed by the US Surgeon General</li>
      <li class="tight">Research shows it is most effective when used 25-40 hours per week.</li>
    </ul>
    <div class="session-photo" role="img" aria-label="Photo of a therapist working one-on-one with a boy at a table using picture cards"></div>
  </section>

  <div class="ribbon help-ribbon">
    <svg width="366" height="52" viewBox="0 0 366 52">
      <polygon points="0,4 22,4 22,50 0,50 12,27" fill="var(--blue)"/>
      <polygon points="344,4 366,4 354,27 366,50 344,50" fill="var(--blue)"/>
      <polygon points="22,50 34,44 34,50" fill="var(--blue-dark)"/>
      <polygon points="332,44 344,50 332,50" fill="var(--blue-dark)"/>
      <rect x="22" y="0" width="322" height="44" fill="var(--blue)"/>
    </svg>
    <span>How We Can Help</span>
  </div>

  <div class="ribbon difference-ribbon">
    <svg width="366" height="52" viewBox="0 0 366 52">
      <polygon points="0,4 22,4 22,50 0,50 12,27" fill="var(--blue)"/>
      <polygon points="344,4 366,4 354,27 366,50 344,50" fill="var(--blue)"/>
      <polygon points="22,50 34,44 34,50" fill="var(--blue-dark)"/>
      <polygon points="332,44 344,50 332,50" fill="var(--blue-dark)"/>
      <rect x="22" y="0" width="322" height="44" fill="var(--blue)"/>
    </svg>
    <span>The Beacon Point Difference</span>
  </div>

  <div class="copy help-copy">
    <p><em>As the only center</em> in Michiana for Autism with an award-winning management team, we know it is our child and family focused philosophy that helps us achieve enduring success. Having been in your shoes, it is our understanding that helps our parents stay strong and positive amidst daily challenges.</p>
  </div>

  <ul class="feature-list difference-list">
    <li>Community based and family focused</li>
    <li>Intensive, daily center based ABA therapy</li>
  </ul>

  <div class="team-photo" role="img" aria-label="Group photo of the therapy team and children standing on a grassy field with autumn trees behind"></div>

  <div class="copy approach-copy">
    <p><em>We make every effort to help</em> families of children with autism through the use of intensive, center based, one-on-one ABA Therapy. This approach can help teach children social, moto, communication and self-help skills.</p>
    <p><em>ABA works</em> – from an 11 year old child who used the restroom for the first time to a 5 year old transitioning back to school – we see success through ABA every day.</p>
  </div>

  <ul class="feature-list service-list">
    <li>We do all insurance billing and processing</li>
    <li>No upfront costs</li>
    <li>Full time onsite BCBA supervision</li>
    <li>Open year round</li>
  </ul>

</main>
</body>
</html>
```